Medigap Insurance Interactive website

We are looking at redesigning our website for a more up to date and responsive look and feel. We will code this site using Bootstrap 3 so please research and know how to design for this. Attached is our logo and a wireframe for the new site.
I look forward to seeing what you guys can do.

Target Market(s)

People elegible for Medigap Insurance in the US

Industry/Entity Type

Insurance

Number of Pages Required

5+ page

Font styles to use
Sans Serif

Requirements
Must have
• Match the logo
• Be Bootstrap 3 compatible design
• Font Awesome Icons

```html
<!DOCTYPE html>
<html lang="en">
<head>
<meta charset="utf-8">
<title>Carebridge360 – Medicare Supplement</title>
<link href="https://fonts.googleapis.com/css2?family=Noto+Serif:wght@400;700&family=Open+Sans:wght@400;600&display=swap" rel="stylesheet">
<style>
:root{
  --red:#b5191c;
  --navy:#0f2c66;
  --grey-band:#e8e8e8;
  --text:#555;
  --white:#fff;
  --icon-grey:#e4e4e4;
}
*{margin:0;padding:0;box-sizing:border-box}
html,body{width:770px;height:1200px;overflow:hidden;background:var(--white)}
body{position:relative;font-family:"Open Sans",sans-serif;color:var(--text)}
.serif{font-family:"Noto Serif",serif}
.abs{position:absolute}

/* header */
.brand{left:50px;top:8px;font-family:"Noto Serif",serif;font-size:33px;color:var(--red);letter-spacing:.5px;line-height:44px}
.tagline{left:388px;top:11px;font-family:"Noto Serif",serif;font-size:14px;color:var(--navy)}
.phone-ring{left:353px;top:29px;width:36px;height:36px;border:1.5px solid var(--red);border-radius:50%;display:flex;align-items:center;justify-content:center}
.phone-num{left:397px;top:30px;font-family:"Noto Serif",serif;font-size:21px;color:var(--red)}
.divider{left:556px;top:14px;width:1px;height:44px;background:#ccc}
.social-dot{width:31px;height:31px;border-radius:50%;background:var(--icon-grey);top:20px}
.social-dot.first{background:var(--red)}

/* nav */
.main-nav{left:0;top:71px;width:770px;height:36px;background:var(--navy);display:flex;align-items:center;padding-left:50px}
.main-nav a{font-family:"Noto Serif",serif;font-size:11.5px;color:var(--white);text-decoration:none;padding:0 21px;height:36px;line-height:36px}
.main-nav a.active{background:var(--red)}

/* hero */
.hero{left:0;top:107px;width:770px;height:406px;background:linear-gradient(120deg,#9aa9bb 0%,#e8edf2 40%,#f7f9fb 60%,#c6cfd9 100%)}

/* welcome */
.welcome{left:0;top:534px;width:770px;text-align:center}
.welcome h1{font-family:"Noto Serif",serif;font-weight:400;font-size:29px;color:var(--red)}
.welcome h1 span{color:var(--navy)}
.welcome p{width:560px;margin:8px auto 0;font-size:10.4px;line-height:16px}
.btn{display:inline-block;background:var(--red);color:var(--white);font-family:"Noto Serif",serif;text-decoration:none}
.btn-buy{margin-top:12px;padding:0 21px;height:33px;line-height:33px;font-size:15px}

/* features */
.features{left:0;top:706px;width:770px;height:167px;background:var(--grey-band)}
.feature{position:absolute;top:29px;width:160px;text-align:center}
.feature .disc{width:80px;height:80px;border-radius:50%;background:var(--white);margin:0 auto;display:flex;align-items:center;justify-content:center}
.feature h3{font-family:"Noto Serif",serif;font-weight:400;font-size:15.5px;color:var(--navy);margin-top:8px}

/* columns */
.col{top:903px;width:200px}
.col h2{font-family:"Noto Serif",serif;font-weight:400;font-size:18px;color:var(--navy);white-space:nowrap}
.col p{font-size:9.6px;line-height:15.5px;margin-top:6px}
.author{font-size:9.6px;color:var(--red);margin-top:5px}
.btn-sub{position:absolute;height:26px;line-height:26px;padding:0 12px;font-size:12.5px}
.email-field{left:285px;top:982px;width:200px;height:27px;border:1px solid #ccc;font-size:9.6px;padding-left:8px;line-height:25px;color:#666}
.video{left:520px;top:937px;width:201px;height:133px;background:radial-gradient(circle,#e2e2e2 0%,#b3b3b3 100%)}

/* footer */
.footer{left:0;top:1126px;width:770px;height:74px;background:var(--red)}
.footer-links{left:50px;top:1141px;display:flex;gap:24px}
.footer-links a{color:var(--white);font-size:10.4px;text-decoration:none}
.footer-links a.home{text-decoration:underline}
.copyright{left:50px;top:1167px;color:var(--white);font-size:10.4px}
.foot-dot{top:1146px;width:34px;height:34px;border-radius:50%;background:#d0292c}
.foot-dot.first{background:var(--white)}
</style>
</head>
<body>

<header>
  <div class="abs brand">CAREBRIDGE360</div>
  <div class="abs tagline">Campare Rates and Save</div>
  <div class="abs phone-ring">
    <svg width="18" height="18" viewBox="0 0 24 24"><path fill="#b5191c" d="M6.6 10.8a15.1 15.1 0 0 0 6.6 6.6l2.2-2.2c.3-.3.7-.4 1-.2 1.1.4 2.3.6 3.6.6.6 0 1 .4 1 1V20c0 .6-.4 1-1 1C10.6 21 3 13.4 3 4c0-.6.4-1 1-1h3.5c.6 0 1 .4 1 1 0 1.3.2 2.5.6 3.6.1.3 0 .7-.2 1z"/></svg>
  </div>
  <div class="abs phone-num">(888) 555 - 0142</div>
  <div class="abs divider"></div>
  <div class="abs social-dot first" style="left:567px"></div>
  <div class="abs social-dot" style="left:607px"></div>
  <div class="abs social-dot" style="left:648px"></div>
  <div class="abs social-dot" style="left:689px"></div>
</header>

<nav class="abs main-nav">
  <a class="active" href="#">Medicare Supplement</a>
  <a href="#">Part D</a>
  <a href="#">How To Decide</a>
  <a href="#">Learn Online</a>
  <a href="#">Why Carebridge 360</a>
  <a href="#">Buy Now</a>
</nav>

<div class="abs hero" role="img" aria-label="Photo of an advisor shaking hands with clients across an office desk"></div>

<section class="abs welcome">
  <h1>Welcome to <span>Carebridge 360</span></h1>
  <p>Lorem Ipsum is simply dummy text of the printing and typesetting industry. Lorem Ipsum has been the industry's standard dummy text ever since the 1500s, when an unknown printer took a galley of type and scrambled it to make a type specimen book.</p>
  <a class="btn btn-buy" href="#">BUY NOW</a>
</section>

<section class="abs features">
  <div class="feature" style="left:45px">
    <div class="disc"><svg width="34" height="34" viewBox="0 0 24 24"><path fill="none" stroke="#b5191c" stroke-width="2" stroke-linejoin="round" d="M3 10h4v11H3zM7 11l4-8c1.5 0 2.5 1 2.2 2.6L12.6 9H19c1.2 0 2 1 1.8 2.2l-1.4 7.6c-.2 1.3-1.2 2.2-2.5 2.2H7"/></svg></div>
    <h3>Compare Rates</h3>
  </div>
  <div class="feature" style="left:219px">
    <div class="disc"><svg width="36" height="34" viewBox="0 0 24 24"><path fill="#b5191c" d="M1 3h4l.7 3H22l-2.5 8H7.7l.5 2H20v2H6.6L3.4 5H1z"/><circle cx="9" cy="20.5" r="1.8" fill="#b5191c"/><circle cx="18" cy="20.5" r="1.8" fill="#b5191c"/></svg></div>
    <h3>Buy Now</h3>
  </div>
  <div class="feature" style="left:393px">
    <div class="disc"><svg width="40" height="32" viewBox="0 0 26 20"><rect x="4" y="2" width="18" height="12" rx="1" fill="none" stroke="#b5191c" stroke-width="2"/><path fill="#b5191c" d="M1 16h24v1.5c0 .8-.7 1.5-1.5 1.5h-21C1.7 19 1 18.3 1 17.5z"/></svg></div>
    <h3>Learn online</h3>
  </div>
  <div class="feature" style="left:566px">
    <div class="disc"><span class="serif" style="font-size:40px;font-weight:700;color:var(--red);line-height:1">?</span></div>
    <h3>Get Expert Help</h3>
  </div>
</section>

<section class="abs col" style="left:50px">
  <h2>What People Are Saying</h2>
  <p>I had a great experience but beware of the Carebridge360 IT Team. You never know what you're gonna get. And that's all I have to say about that.</p>
  <div class="author">- Dana Whitfield</div>
</section>
<a class="btn btn-sub" href="#" style="left:50px;top:1018px">SUBSCRIBE</a>

<section class="abs col" style="left:286px">
  <h2>Monthly Updates</h2>
  <p>Enter Email for Customized Monthly Rate Updates and More</p>
</section>
<div class="abs email-field">Enter Email Id</div>
<a class="btn btn-sub" href="#" style="left:285px;top:1018px">SUBSCRIBE</a>

<section class="abs col" style="left:522px">
  <h2>Why Carebridge360</h2>
</section>
<div class="abs video" role="img" aria-label="Video thumbnail introducing Carebridge360"></div>

<footer class="abs footer"></footer>
<div class="abs footer-links">
  <a class="home" href="#">Carebridge360</a>
  <a href="#">Sitemap</a>
  <a href="#">Buy Now</a>
  <a href="#">Blog</a>
  <a href="#">Login</a>
</div>
<div class="abs copyright">© Carebridge360 - 2016. All Rights Reserved.</div>
<div class="abs foot-dot first" style="left:546px"></div>
<div class="abs foot-dot" style="left:592px"></div>
<div class="abs foot-dot" style="left:639px"></div>
<div class="abs foot-dot" style="left:686px"></div>

</body>
</html>
```